Structural Engineering Business Card

Veltrow Drafts does residential house plans for clients in Central Florida. Would like simple but elegant business card that is appropriate for a house plan engineering company. Prefer black business card with black/white them but open to other shades of blue. I uploaded a sample card that I came across that looked good but please come up with your own creative designs.

Contact Information for Business Card

Name, Title, Phone, Email, Address, website

```html
<!DOCTYPE html>
<html lang="en">
<head>
<meta charset="utf-8">
<title>Veltrow Drafts – Business Card</title>
<link rel="stylesheet" href="https://fonts.googleapis.com/css2?family=Arimo:wght@400;700&display=swap">
<style>
  :root {
    --page-bg: #2a2a2a;
    --card-bg: #1c1c1c;
    --region-grey: #333333;
    --region-dark: #242424;
    --ink: #ffffff;
    --ink-soft: #d8d8d8;
  }
  * { margin: 0; padding: 0; box-sizing: border-box; }
  html, body {
    width: 1200px; height: 900px; overflow: hidden;
    background: var(--page-bg);
    font-family: "Arimo", Arial, sans-serif;
  }
  .stage {
    width: 1200px; height: 900px;
    display: flex; align-items: center; justify-content: center;
  }
  .card {
    position: relative;
    width: 1000px; height: 572px;
    background: var(--card-bg);
    overflow: hidden;
    box-shadow: 0 20px 50px rgba(0,0,0,.55);
    color: var(--ink);
  }
  .region-band {
    position: absolute; top: 0; right: 0;
    width: 150px; height: 100%;
    background: var(--region-dark);
  }
  .region-art {
    position: absolute; top: 70px; left: 560px;
    width: 330px; height: 502px;
    background: linear-gradient(180deg, #383838 0%, var(--region-grey) 100%);
    border-radius: 28px 28px 0 0;
  }
  .brand {
    position: absolute; top: 92px; left: 270px;
    display: flex; align-items: center; gap: 16px;
  }
  .brand-dot {
    width: 26px; height: 26px; background: var(--ink);
  }
  .brand-name {
    font-weight: 700; font-size: 56px; letter-spacing: .5px;
    text-transform: uppercase; color: var(--ink);
  }
  .person {
    position: absolute; top: 220px; left: 140px;
  }
  .person-name {
    font-weight: 700; font-size: 30px; letter-spacing: 1px; text-transform: uppercase;
  }
  .person-title {
    font-size: 22px; color: var(--ink-soft); margin-top: 2px;
  }
  .contacts {
    position: absolute; top: 310px; left: 110px;
    list-style: none; font-size: 22px; line-height: 34px;
  }
  .contacts li { display: flex; align-items: center; gap: 10px; }
  .contacts svg { width: 18px; height: 18px; fill: var(--ink); }
  .divider {
    position: absolute; top: 412px; left: 420px;
    width: 2px; height: 70px; background: var(--ink);
    transform: rotate(20deg);
  }
  .address {
    position: absolute; top: 420px; left: 460px;
    font-style: normal; font-size: 22px; line-height: 30px;
  }
</style>
</head>
<body>
<main class="stage">
  <article class="card">
    <div class="region-band"></div>
    <div class="region-art" role="img" aria-label="Large grey silhouette map of Florida as a background decoration"></div>

    <div class="brand">
      <span class="brand-dot"></span>
      <span class="brand-name">Veltrow Drafts</span>
    </div>

    <div class="person">
      <p class="person-name">Marcus Delaine</p>
      <p class="person-title">Founder/CEO</p>
    </div>

    <ul class="contacts">
      <li>
        <svg viewBox="0 0 24 24" aria-hidden="true"><path d="M6.6 10.8a15.1 15.1 0 0 0 6.6 6.6l2.2-2.2c.3-.3.7-.4 1-.2 1.1.4 2.3.6 3.6.6.6 0 1 .4 1 1V20c0 .6-.4 1-1 1A17 17 0 0 1 3 4c0-.6.4-1 1-1h3.5c.6 0 1 .4 1 1 0 1.3.2 2.5.6 3.6.1.3 0 .7-.2 1z"/></svg>
        555.318.2740
      </li>
      <li>
        <svg viewBox="0 0 24 24" aria-hidden="true"><path d="M2 5h20v14H2z M2 5l10 8 10-8" stroke="#1c1c1c" stroke-width="1.5"/></svg>
        info@veltrowdrafts.com
      </li>
      <li>
        <svg viewBox="0 0 24 24" aria-hidden="true"><circle cx="12" cy="12" r="10"/><path d="M2 12h20M12 2c3 3 3 17 0 20M12 2c-3 3-3 17 0 20" stroke="#1c1c1c" stroke-width="1.4" fill="none"/></svg>
        www.veltrowdrafts.com
      </li>
    </ul>

    <span class="divider"></span>
    <address class="address">
      2190 Harbor Way Suite 310<br>
      Orlando, FL 32801
    </address>
  </article>
</main>
</body>
</html>
```